Production Company Needs Poster for Feature Film

We need a poster for a thriller/horror film that will be released on Vuremix. We would like something that is 1- simple and 2- looks professionally done.

In the movie Jo (female lead) finds out the devil wants to use her suffering (loss of entire family) to open a portal and escape into our world. If the devil gets loose he will kill millions. Jo is befriended by Mark (male lead) and Mike (supporting male lead). They are a team of sufferer hunters who find people like Jo (the sufferer) and help them close the portal before the devil escapes. In order to close the portal they must find 2 objects and destroy them. During their hunt Mike is accidently killed by Mark while they are saving Jo from the devil's underlings. Mark is then captured and must be rescued by Jo. It turns out that Mike was previously captured and tortured by the devil until he agreed to work for him. Mike is planning on handing Jo over to the devil, but must be stopped by Mark and Jo.

The trailer can be found at https://www.clipvane.example/watch?v=k-tQzRB8Mun

Attached are a number of uncorrected pictures of the 3 leads. Each picture is labeled with the name of the characters from left to right. Note it is NOT a requirement to use these pictures. They are provided if the designer desires to use them.

Target Market(s)

Independent horror/thriller movie fans. 18-30 years old, technically savvy, consumes much of their content on their phone or computer.

Industry/Entity Type

It Company

Requirements
Must have
• The poster must include the title of the movie "The Hollowing" in large, legible print. Since the poster is for Vuremix it is important that the words and the theme are easily understood when it is shown as a thumbnail on the Vuremix website on a computer of phone.
• The final image needs to conform to the requirements below.
• - RGB color space with 1400x2100 pixels minimum size (2:3 ratio) 
Nice to have
• Custom lettering that fits the theme of the poster.
• Beyond that we are purposely not providing additional artistic input/design requirements. We want to see maximum creativity from the designers and want a range of options.
Should not have
• It should not have small lettering or details that won't translate well when the image is displayed as a thumbnail. Do not use a standard font (serif, times new roman...).

```html
<!DOCTYPE html>
<html lang="en">
<head>
<meta charset="utf-8">
<title>The Hollowing — Poster</title>
<link href="https://fonts.googleapis.com/css2?family=Bebas+Neue&family=Rubik+Dirt&display=swap" rel="stylesheet">
<style>
  :root {
    --night: #000000;
    --glow-core: #fbf8ee;
    --glow-mid: #e9dcc0;
    --glow-edge: #6b4a2c;
    --blood: #8e0d17;
    --credit-ink: #7a0c12;
    --credit-dark: #2a0506;
    --cast-ink: #f2ece0;
    --skin-light: #8a6c52;
    --skin-mid: #4e3727;
    --skin-dark: #1e140d;
  }
  * { margin: 0; padding: 0; box-sizing: border-box; }
  html, body { width: 800px; height: 1200px; overflow: hidden; background: var(--night); }
  .poster {
    position: relative;
    width: 800px;
    height: 1200px;
    background: var(--night);
    overflow: hidden;
  }
  .portrait {
    position: absolute;
    top: 470px;
    width: 300px;
    height: 560px;
  }
  .portrait--left {
    left: 0;
    background: radial-gradient(ellipse 75% 50% at 25% 52%, var(--skin-light) 0%, var(--skin-mid) 40%, var(--skin-dark) 70%, var(--night) 100%);
  }
  .portrait--right {
    right: 0;
    background: radial-gradient(ellipse 75% 50% at 75% 52%, var(--skin-light) 0%, var(--skin-mid) 40%, var(--skin-dark) 70%, var(--night) 100%);
  }
  .light-band {
    position: absolute;
    left: 278px;
    top: 0;
    width: 244px;
    height: 1060px;
    background:
      linear-gradient(to bottom, rgba(0,0,0,0) 82%, rgba(0,0,0,0.85) 100%),
      linear-gradient(to right, var(--glow-edge) 0%, var(--glow-mid) 12%, var(--glow-core) 35%, var(--glow-core) 65%, var(--glow-mid) 88%, var(--glow-edge) 100%);
    box-shadow: 0 0 40px rgba(240,225,190,0.35);
  }
  .title {
    position: absolute;
    left: 278px;
    top: 60px;
    width: 244px;
    height: 560px;
    font-family: 'Bebas Neue', sans-serif;
    font-weight: 400;
    color: var(--blood);
    text-align: center;
  }
  .title__article {
    display: block;
    font-size: 64px;
    line-height: 70px;
    letter-spacing: 10px;
    padding-left: 10px;
  }
  .title__word {
    position: absolute;
    left: 0;
    top: 82px;
    width: 244px;
    height: 470px;
    display: flex;
    align-items: center;
    justify-content: center;
  }
  .title__word span {
    writing-mode: vertical-rl;
    font-size: 150px;
    line-height: 150px;
    letter-spacing: 1px;
  }
  .writers {
    position: absolute;
    left: 278px;
    top: 632px;
    width: 244px;
    text-align: center;
    font-family: 'Rubik Dirt', sans-serif;
    color: var(--credit-ink);
    text-transform: uppercase;
  }
  .writers .label { font-size: 22px; line-height: 30px; }
  .writers .name { font-size: 30px; line-height: 38px; color: var(--credit-dark); }
  .writers .joiner { font-size: 22px; line-height: 32px; }
  .cast {
    position: absolute;
    left: 0;
    top: 1068px;
    width: 800px;
    text-align: center;
    font-family: 'Rubik Dirt', sans-serif;
    color: var(--cast-ink);
    text-transform: uppercase;
    font-size: 34px;
    line-height: 42px;
  }
  .cast .joiner { font-size: 28px; }
</style>
</head>
<body>
  <main class="poster">
    <div class="portrait portrait--left" role="img" aria-label="Close-up photograph of the female lead with hollow black eyes, half visible at the left edge"></div>
    <div class="portrait portrait--right" role="img" aria-label="Mirrored close-up photograph of the female lead with hollow black eyes, half visible at the right edge"></div>
    <div class="light-band"></div>

    <h1 class="title" aria-label="The Hollowing">
      <span class="title__article">THE</span>
      <span class="title__word"><span>HOLLOWING</span></span>
    </h1>

    <section class="writers">
      <p class="label">Written by</p>
      <p class="name">Cal Ridley</p>
      <p class="joiner">and</p>
      <p class="name">Owen Marsh</p>
    </section>

    <section class="cast">
      <p>Margaret Hale</p>
      <p>Vince Callahan</p>
      <p><span class="joiner">and</span> DaMarcus Reed</p>
    </section>
  </main>
</body>
</html>
```